Business card and letterhead design

Using both 1st and 2nd selected logo designs we need to generate a business cards that use the combined logo for BRVSN/Quorvantideworks together and corporate letterhead for both company logos independently and one combined, "same design just swap out logos". Result will be 1) BRVSN/Quorvantideworks Business cards- The flip side of the business card will be a photo of one of our custom homes with our slogan on it "we will provide" (2) Corporate letterhead for BRVSN/Quorvantideworks (3) Corporate letterhead for BRVSN (4) Corporate letterhead Quorvantideworks. We will upload criteria for the other project "marketing brochure" soon, still need to edit the payment to be similar to this one both first place and runner up.
All letter head and business cards and brochures should have consistent look / feel / theme.
Updates

                                        Logos and images plus more criteria have been uploaded for project folder.

Target Market(s)

The examples of consistent theme ...... are not to be exactly what we are looking for but just to convey the idea of the overall concept of branding throughout. We just included them for reference and not for specifically that we liked any of them. So the business cards, letterhead and then the envelopes and marketing brochures well all tie together. Also attached is the sample of our website homepage although the bottom is cropped off.

Industry/Entity Type

Business

Requirements
Must have
• We need both BRVSN logo and Quorvantideworks logo together for the business card. Will consider one company on one side and other on back side, this is the way we have them now. Basically the BRVSN is the local architecture firm and quorvan is the online company for stock plan sales. Will have same phone number. Each employee will have a card and their email address plus the toll free number. The letterhead will have mailing address
P.O. Box 208674, The Woodlands, TX 77529. We would like to maybe put a photo on one side if we don't do the flip one company one each side.
Nice to have
• Our company logo is "Designing Homes That Fit Your Lifestyle"

```html
<!DOCTYPE html>
<html lang="en">
<head>
<meta charset="utf-8">
<title>BRVSN / Quorvantideworks Business Card</title>
<link href="https://fonts.googleapis.com/css2?family=Open+Sans:ital,wght@0,400;0,700;1,400&display=swap" rel="stylesheet">
<style>
  :root {
    --page: #ffffff;
    --card-dark: #1d1e1c;
    --glow: #f2e23a;
    --gold: #d8b418;
    --logo-bg: #0b0c0a;
    --logo-rule: #c9c9c9;
    --band: #000000;
    --white: #ffffff;
    --yellow: #f7c21a;
    --yellow-light: #fde27a;
    --night: #283246;
    --night-deep: #141a26;
  }
  * { margin: 0; padding: 0; box-sizing: border-box; }
  html, body { width: 954px; height: 1200px; overflow: hidden; background: var(--page); }
  body { position: relative; font-family: "Open Sans", Arial, sans-serif; }

  .card { position: absolute; overflow: hidden; }

  /* Front: BRVSN */
  .card-front {
    left: 175px; top: 183px; width: 716px; height: 359px;
    background: radial-gradient(ellipse 230px 190px at 50% 44%, var(--glow) 0%, #8f8a25 45%, var(--card-dark) 100%);
  }
  .logo-plate {
    position: absolute; background: var(--logo-bg);
    display: flex; align-items: center; justify-content: center;
  }
  .card-front .logo-plate {
    left: 161px; top: 75px; width: 394px; height: 142px;
    border: 1px solid var(--logo-rule);
  }
  .brand-name { color: var(--gold); font-weight: 700; line-height: 1; }
  .card-front .brand-name { font-size: 64px; letter-spacing: 2px; }
  .tagline-band {
    position: absolute; left: 2px; top: 313px; width: 708px; height: 39px;
    background: var(--band); color: var(--white);
    font-style: italic; font-size: 24px; line-height: 39px; text-align: center;
  }

  /* Back: Quorvantideworks */
  .card-back { left: 179px; top: 591px; width: 714px; height: 340px; }
  .card-back svg { position: absolute; left: 0; top: 0; }
  .holder-name {
    position: absolute; left: 38px; top: 34px;
    color: var(--white); font-weight: 700; font-size: 24px;
  }
  .contact-block {
    position: absolute; left: 402px; top: 24px;
    color: var(--white); font-weight: 700; font-size: 20px; line-height: 27px;
  }
  .card-back .logo-plate {
    left: 40px; top: 179px; width: 417px; height: 143px;
  }
  .card-back .brand-name { font-size: 40px; }
</style>
</head>
<body>

  <section class="card card-front">
    <div class="logo-plate"><span class="brand-name">BRVSN</span></div>
    <p class="tagline-band">Designing Homes That Fit Your Lifestyle..</p>
  </section>

  <section class="card card-back">
    <svg width="714" height="340" viewBox="0 0 575 274" preserveAspectRatio="none">
      <defs>
        <linearGradient id="night-sky" x1="0" y1="0" x2="0" y2="1">
          <stop offset="0" stop-color="var(--night)"/>
          <stop offset="1" stop-color="var(--night-deep)"/>
        </linearGradient>
        <linearGradient id="sun-fill" x1="0" y1="0" x2="1" y2="1">
          <stop offset="0" stop-color="var(--yellow)"/>
          <stop offset="0.6" stop-color="var(--yellow-light)"/>
          <stop offset="1" stop-color="var(--yellow)"/>
        </linearGradient>
      </defs>
      <rect x="0" y="0" width="575" height="274" fill="var(--card-dark)"/>
      <rect x="6" y="8" width="562" height="266" fill="url(#night-sky)" role="img" aria-label="Photo of a custom luxury home at dusk"/>
      <path d="M0 100 C140 125 280 145 380 195 C470 240 540 140 575 48 L575 274 L0 274 Z" fill="url(#sun-fill)"/>
      <path d="M0 94 C140 119 280 139 380 189 C470 234 540 134 575 42" fill="none" stroke="var(--white)" stroke-width="7"/>
    </svg>
    <p class="holder-name">First name,Last name</p>
    <p class="contact-block">
      Address Line1,<br>
      Address Line 2,<br>
      Any city,state.<br>
      Phone :(555)111-2222<br>
      Fax :(555)111-3333
    </p>
    <div class="logo-plate"><span class="brand-name">Quorvantideworks</span></div>
  </section>

</body>
</html>
```